Home Care App Design

We would like a responsive app design (mobile/web) for an app that will be used by our staff. These need to work display nearly the same for iPhone and Android. The app tracks caregiver tasks (check-in time, daily client activities, caregiver notes, and check out time) and provides updates to team and family members
Updates

I have added individual or grouped pages with better resolution. please let me know if you have any questions

we did not get enough entries so we increase the budget and have not received any new designer entries

Target Market(s)

professional caregivers and family members

Industry/Entity Type

Home Health Care

Font styles to use
Serif

Requirements
Must have
• We currently have a logo - please use colors or slight variants
• We also will need pop-up designs for informational messages and call to actions (with 1-3 options)
Nice to have
• I have attached a sketch of the app, please use this as a guideline. We are looking for ease of use.
• Please feel free to add design aspects that will make it easy to navigate, select options, or enter notes/messages

```html
<!DOCTYPE html>
<html lang="en">
<head>
<meta charset="utf-8">
<title>Carenest – App Screens</title>
<link rel="stylesheet" href="https://fonts.googleapis.com/css2?family=Montserrat:wght@400;600;700&family=Open+Sans:wght@300;400;600;700&display=swap">
<style>
  :root{
    --board:#4b4b4b;
    --brand:#5bbde3;
    --brand-dark:#3f6b86;
    --white:#ffffff;
    --paper:#f1f1f1;
    --ink:#333333;
    --ink-soft:#555555;
    --rule:#d8d8d8;
    --happy:#7cc242;
    --neutral:#f7a823;
    --sad:#e8262a;
  }
  *{box-sizing:border-box;margin:0;padding:0}
  html,body{width:721px;height:1200px;overflow:hidden}
  body{background:var(--board);position:relative;font-family:"Open Sans",Arial,sans-serif;color:var(--ink)}
  .screen{position:absolute;width:307px;background:var(--white);overflow:hidden}
  .screen--login{left:29px;top:29px;height:560px;background:var(--brand)}
  .screen--comments{left:365px;top:29px;height:560px}
  .screen--rating{left:29px;top:619px;height:552px}
  .screen--send{left:365px;top:619px;height:552px}

  .abs{position:absolute}

  /* login */
  .login-title{left:0;right:0;top:52px;text-align:center;color:var(--white);font-family:"Montserrat",sans-serif;font-size:28px;font-weight:400}
  .login-brand{left:0;right:0;top:150px;text-align:center;color:var(--white);font-family:"Montserrat",sans-serif;font-weight:600;font-size:30px}
  .field{left:29px;width:259px;height:46px;background:var(--white);font-size:12px;color:var(--ink);padding:0 12px;display:flex;align-items:center;letter-spacing:.3px}
  .field--user{top:269px}
  .field--pass{top:331px}
  .login-button{left:29px;top:398px;width:259px;height:53px;background:var(--brand-dark);color:var(--white);font-family:"Montserrat",sans-serif;font-weight:700;font-size:15px;display:flex;align-items:center;justify-content:center;letter-spacing:.5px}

  /* header bar */
  .app-bar{left:0;top:0;width:100%;background:var(--brand);color:var(--white);display:flex;align-items:center}
  .app-bar--short{height:43px;padding-left:14px;gap:8px;font-family:"Montserrat",sans-serif;font-weight:700;font-size:14px;letter-spacing:.5px}
  .app-bar--tall{height:62px;padding:0 14px}

  /* comments */
  .comment-title{left:24px;font-family:"Montserrat",sans-serif;font-weight:700;font-size:12px;color:var(--ink)}
  .comment-box{left:24px;width:259px;background:var(--paper);font-size:12px;line-height:17px;color:var(--ink-soft);padding:16px 18px}

  /* rating */
  .bar-mark{width:22px;height:22px;border-radius:50%;background:var(--white);flex:none}
  .bar-text{margin-left:12px;flex:1}
  .bar-text strong{display:block;font-family:"Montserrat",sans-serif;font-size:13px;font-weight:700}
  .bar-text span{display:block;font-size:12px;font-weight:600}
  .intro{left:24px;top:84px;width:262px;font-size:13px;line-height:19px;color:var(--ink)}
  .rate-row{left:0;width:100%;height:0}
  .rate-label{position:absolute;left:24px;top:-9px;font-family:"Montserrat",sans-serif;font-weight:700;font-size:12px}
  .rate-dot{position:absolute;width:42px;height:42px;border-radius:50%;top:-21px}
  .rate-dot--happy{left:106px;background:var(--happy)}
  .rate-dot--neutral{left:176px;background:var(--neutral)}
  .rate-dot--sad{left:243px;background:var(--sad)}
  .divider{left:14px;width:279px;height:1px;background:var(--rule)}
  .outline-button{left:79px;top:466px;width:151px;height:46px;border:1.5px solid var(--sad);color:var(--sad);font-family:"Montserrat",sans-serif;font-weight:600;font-size:12px;display:flex;align-items:center;justify-content:center}

  /* send */
  .bar-name{font-family:"Montserrat",sans-serif;font-weight:600;font-size:24px;color:var(--white)}
  .send-label{left:29px;top:89px;font-size:12px;font-weight:600;color:var(--ink)}
  .send-target{left:29px;top:113px;font-size:12px;font-weight:700;color:var(--ink)}
  .message-box{left:24px;top:149px;width:259px;height:360px;background:var(--paper);padding:20px 18px;font-size:12px;line-height:17px;color:var(--ink-soft)}
  .message-box p+p{margin-top:16px}
</style>
</head>
<body>

<section class="screen screen--login">
  <h1 class="abs login-title">Login</h1>
  <div class="abs login-brand">Carenest</div>
  <div class="abs field field--user">USER NAME</div>
  <div class="abs field field--pass">PASSWORD</div>
  <div class="abs login-button">LOGIN</div>
</section>

<section class="screen screen--comments">
  <header class="abs app-bar app-bar--short">
    <svg width="12" height="14" viewBox="0 0 12 14"><path d="M9 1 3 7l6 6" fill="none" stroke="#fff" stroke-width="2.5"/></svg>
    COMMENTS
  </header>
  <h2 class="abs comment-title" style="top:79px">LOREM IPSUM</h2>
  <div class="abs comment-box" style="top:106px;height:134px">Lorem ipsum dolor sit amet, consectetur adipiscing elit, sed do eiusmod tempor incididunt ut labore et dolore.</div>
  <h2 class="abs comment-title" style="top:278px">LOREM IPSUM</h2>
  <div class="abs comment-box" style="top:302px;height:96px">Lorem ipsum dolor sit amet, consectetur adipiscing elit, sed do eiusmod tempor.</div>
  <h2 class="abs comment-title" style="top:415px">LOREM IPSUM</h2>
  <div class="abs comment-box" style="top:444px;height:84px">Lorem ipsum dolor sit amet, consectetur adipiscing elit.</div>
</section>

<section class="screen screen--rating">
  <header class="abs app-bar app-bar--tall">
    <span class="bar-mark"></span>
    <div class="bar-text"><strong>LOREM</strong><span>Lorem Ipsum is simply.</span></div>
    <svg width="12" height="18" viewBox="0 0 12 18"><path d="M2 2l7 7-7 7" fill="none" stroke="#fff" stroke-width="2.5"/></svg>
  </header>
  <p class="abs intro">Lorem Ipsum is simply dummy text of the printing and typesetting</p>

  <div class="abs rate-row" style="top:192px">
    <span class="rate-label">LOREM</span>
    <span class="rate-dot rate-dot--happy" role="img" aria-label="Good rating"></span>
    <span class="rate-dot rate-dot--neutral" role="img" aria-label="Neutral rating"></span>
    <span class="rate-dot rate-dot--sad" role="img" aria-label="Poor rating"></span>
  </div>
  <div class="abs divider" style="top:240px"></div>
  <div class="abs rate-row" style="top:286px">
    <span class="rate-label">LOREM</span>
    <span class="rate-dot rate-dot--happy" role="img" aria-label="Good rating"></span>
    <span class="rate-dot rate-dot--neutral" role="img" aria-label="Neutral rating"></span>
    <span class="rate-dot rate-dot--sad" role="img" aria-label="Poor rating"></span>
  </div>
  <div class="abs divider" style="top:331px"></div>
  <div class="abs rate-row" style="top:374px">
    <span class="rate-label">LOREM</span>
    <span class="rate-dot rate-dot--happy" role="img" aria-label="Good rating"></span>
    <span class="rate-dot rate-dot--neutral" role="img" aria-label="Neutral rating"></span>
    <span class="rate-dot rate-dot--sad" role="img" aria-label="Poor rating"></span>
  </div>
  <div class="abs divider" style="top:418px"></div>
  <div class="abs outline-button">LOREM IPSUM</div>
</section>

<section class="screen screen--send">
  <header class="abs app-bar app-bar--tall">
    <span class="bar-name">Carenest</span>
  </header>
  <div class="abs send-label">SEND TO</div>
  <div class="abs send-target">@TEAM@FAMILY</div>
  <div class="abs message-box">
    <p>Lorem ipsum dolor sit amet, consectetur adipiscing.</p>
    <p>Lorem ipsum dolor sit amet, consectetur adipiscing elit, sed do eiusmod tempor incididunt ut labore et dolore magna aliqua. Ut enim ad minim ven iam, quis nostrud exerci tation ullamco laboris nisi ut aliquip ex ea commodo cons equat. Duis aute irure dolor in repr ehenderit in voluptate velit esse cillum dolore.</p>
  </div>
</section>

</body>
</html>
```